Email signatures and letterhead for in-house lawyers and staff

I need Word, Outlook, and Gmail compatible letterhead and email signature block for an in-house litigation group. Simple and generic is the goal! The design must be user-modifiable for several locations and job titles. The design will work best if created in MS Word. We are an in-house group of trial lawyers, about 40 persons total, operating from nine locations, and providing services in ten US states. Letterhead will be used in header of MSWord documents. Email sig will be used in both Outlook and Gmail. The office name will be different in each of our locations, so the design has to be user-modifiable.

Industry/Entity Type

Law Firm

Font styles to use
Sans Serif

Requirements
Must have
• A fresher, more professional look than the screenshots I've posted

The screenshot with multiple attorney names in the office is most representative of the info we want included.
Nice to have
• Sylish but not overly so. Generic legal symbols might be appropriate, but can't look like tired old clip art.
Should not have
• watermarks

```html
<!DOCTYPE html>
<html lang="en">
<head>
<meta charset="utf-8">
<title>Law Office Letterhead and Email Signature</title>
<link href="https://fonts.googleapis.com/css2?family=Signika:wght@300;400&family=Sacramento&display=swap" rel="stylesheet">
<style>
  :root {
    --blue: #2b57b3;
    --brown: #a3733a;
    --brown-dark: #5e4226;
    --ink: #1f1f1f;
    --paper: #ffffff;
    --bg: #ffffff;
  }
  * { margin: 0; padding: 0; box-sizing: border-box; }
  html, body { width: 1200px; height: 1200px; overflow: hidden; background: var(--bg); }
  body { position: relative; font-family: "Signika", sans-serif; color: var(--ink); }

  .sheet { position: absolute; background: var(--paper); box-shadow: 0 4px 14px rgba(0,0,0,.35); overflow: hidden; }

  /* Letterhead */
  .letterhead { left: 88px; top: 163px; width: 683px; height: 883px; }
  .letterhead .firm-name { position: absolute; left: 42px; top: 36px; font-size: 19.5px; color: var(--blue); font-weight: 400; letter-spacing: .2px; }
  .letterhead .firm-mark { position: absolute; left: 35px; top: 72px; width: 44px; height: 44px; background: var(--blue); }
  .letterhead .partners { position: absolute; left: 101px; top: 70px; font-size: 13px; line-height: 16.5px; color: var(--brown); list-style: none; }
  .letterhead .contact { position: absolute; right: 37px; top: 38px; text-align: right; font-size: 10.4px; line-height: 18px; }
  .letterhead .contact .label { color: var(--brown); }
  .letterhead .address { position: absolute; right: 37px; top: 98px; text-align: right; font-size: 10.4px; line-height: 16px; }
  .letterhead .recipient { position: absolute; left: 64px; top: 217px; font-size: 13px; line-height: 25px; }
  .letterhead .body { position: absolute; left: 64px; top: 317px; width: 560px; font-size: 13px; line-height: 25px; }
  .letterhead .body p + p { margin-top: 25px; }
  .letterhead .closing { position: absolute; left: 70px; top: 654px; font-size: 12.5px; }
  .signature { font-family: "Sacramento", cursive; color: var(--blue); white-space: nowrap; }
  .letterhead .signature { position: absolute; left: 66px; top: 666px; font-size: 36px; }
  .footer-band { position: absolute; left: 0; bottom: 0; display: block; }

  /* Email signature */
  .email-signature { left: 362px; top: 451px; width: 776px; height: 307px; }
  .email-signature .signature { position: absolute; left: 50px; top: 14px; font-size: 44px; }
  .email-signature .title { position: absolute; left: 59px; top: 62px; font-size: 16px; color: var(--brown); }
  .email-signature .details { position: absolute; left: 51px; top: 97px; font-size: 10px; line-height: 15.3px; }
  .email-signature .details .label { color: var(--blue); }
  .email-signature .rule { position: absolute; left: 27px; top: 170px; width: 709px; height: 13px; border-radius: 5px; background: var(--blue); }
  .email-signature .fold { position: absolute; left: 0; top: 0; }
  .email-signature .emblem { position: absolute; left: 574px; top: 119px; width: 129px; height: 118px; background: var(--brown); }
  .email-signature .disclaimer { position: absolute; left: 34px; top: 189px; width: 500px; font-size: 6.6px; line-height: 13.6px; }
  .email-signature .disclaimer p + p { margin-top: 14px; }
</style>
</head>
<body>

<section class="sheet letterhead">
  <h1 class="firm-name">LAW OFFICE OF DANIEL R. HARTLEY</h1>
  <div class="firm-mark" aria-hidden="true"></div>
  <ul class="partners">
    <li>Daniel R. Hartley</li>
    <li>Karen L. Ostrow</li>
    <li style="margin-top:4px">Marcus T. Delaney</li>
  </ul>
  <div class="contact">
    <div><span class="label">Phone : </span>555 -010 -2222</div>
    <div><span class="label">Fax : </span>555 -010-3333</div>
    <div><span class="label">Email : </span>counsel@hartley-law.example</div>
  </div>
  <div class="address">
    <div>4100 Lakeview Pkwy, East, Suite 257</div>
    <div>Anytown, XY 99999</div>
  </div>
  <div class="recipient">
    <div>To</div>
    <div>The,</div>
    <div>Director</div>
  </div>
  <div class="body">
    <p>Lorem ipsum dolor sit amet, consectetur adipiscing elit. Fusce vel<br>vulptate dictum, massa quam dapibus leo, eget vulputate orci purus ut<br>ligula. Pellen tesque aliquam quam vel dolor. Nunc adipiscing. Sed quam<br>aliquam molestie varius ac, tellus. Vestibulum ante ipsum primis pellen<br>tesque lorem.</p>
    <p>Curabitur sit amet erat quis risus feugiat viverra. Pellentesque augue justo,<br>venenatis non, arcu. Nunc nec libero. Vestibulum ante ipsum primis in<br>orci. Curabitur dolonunc,egestas at, accumsan at, luctus non, quam. Nam<br>volutpat. Vestibulum ante ipsum primis in faucibus orci luctus et ultrices.<br>Ut sit amet orci vel mauris blandit vehicula. Nullam quis enim. Integer<br>Curabitur in odio.</p>
  </div>
  <p class="closing">Thanking you,</p>
  <div class="signature">Daniel R. Hartley</div>
  <svg class="footer-band" width="683" height="25" viewBox="0 0 683 25" aria-hidden="true">
    <polygon points="418,0 683,0 683,25 400,25" fill="var(--brown)"/>
    <polygon points="0,12 405,12 397,25 0,25" fill="var(--blue)"/>
  </svg>
</section>

<section class="sheet email-signature">
  <div class="signature">Daniel R. Hartley</div>
  <p class="title">Attorney at law</p>
  <div class="details">
    <div>Law Office Of Daniel R. Hartley</div>
    <div><span class="label">T</span> : 555.014.1111| <span class="label">F</span> : 555.014.4444</div>
    <div>daniel.hartley@trial-group.example</div>
    <div>2850 Harbor Ave. East - Suite 575, Anytown, XY 86753</div>
  </div>
  <svg class="fold" width="776" height="307" viewBox="0 0 776 307" aria-hidden="true">
    <polygon points="703,119 737,172 703,172" fill="var(--brown-dark)"/>
    <polygon points="544,185 574,185 574,237" fill="var(--brown-dark)"/>
  </svg>
  <div class="rule"></div>
  <div class="emblem" role="img" aria-label="Scales of justice emblem in white on brown"></div>
  <div class="disclaimer">
    <p>The information contained in this communication from the sender is confidential. It is intended solely for use by the recipient and others authorized to receive it. If you are not the recipient, you are hereby notified that any disclosure, copying, distribution, or taking action in relation to the contents of this information is strictly prohibited and may be unlawful.</p>
    <p>The Law Office of Gregory N. Pace is an unincorporated association of individual licensed attorneys employed by Keystone Mutual Insurance Group for the purpose of representing Keystone Mutual Insurance Group, its policyholders, and insureds.</p>
  </div>
  <svg class="footer-band" width="776" height="22" viewBox="0 0 776 22" aria-hidden="true">
    <polygon points="470,0 776,0 776,22 448,22" fill="var(--brown)"/>
    <polygon points="0,8 462,8 453,22 0,22" fill="var(--blue)"/>
  </svg>
</section>

</body>
</html>
```